Unique Builder wordpress website - Supply Graphics Only

We need a brand new website for a building company in Perth, Australia who constructs insulated panels (sip).
What is a SIP?
A SIP is a high-performance building panel used for floors, walls, and roofs in residential and commercial buildings. Panels are typically made using Expanded Polystyrene (EPS) sandwiched between two structural skins.
The design must incorporate a slick professional look and keep to the logo colours (Lime green & Blacks). The logo must not change colours or be altered. (
We will convert the graphics to a wordpress site. We have our own coders)
Design:
The website design must be clean, mobile friendly and the final design will be adapted to WordPress CMS.
The menus must contain dropdown menus and front page may contain a youtube video at a later date.
Fonts must be clear and easy to read
The contact us page will need to have an online form and google map.
The 16 pages listed will be the complete site and are for reference only. For this project the winning designer would need to supply the Homepage, and 1 inner pages only as PSD files.
The structure is as follows:
Home
About us
High Tech Homes
What is a sip
Benefits
FAQ
Designs
Residential
Granny Flats
Architectural design
Photo Gallery <--- Would be great if a sample design can be provided
Services
Project management and custom design
Site Assembly
Kit Supply
Contact us
***We don't need the designer to design every page however a 1 inner page would be ideal****
Our Competitors websites
Note: the following websites look crap however, the following websites are some of our competitors. We want a clean and awesome layout.
http://www.vortmelbuild.com.au/
http://kelvarostructures.com.au/
http://www.tralinbowerk.net.au/
New home builders and commercial builders
Building
5+ page

```html
<!DOCTYPE html>
<html lang="en">
<head>
<meta charset="utf-8">
<title>Korvanta – Advanced Building Technology</title>
<link rel="stylesheet" href="https://fonts.googleapis.com/css2?family=Raleway:wght@400;500;600&family=Oswald:wght@500&family=Roboto:wght@300;400;500&display=swap">
<style>
:root{
  --lime:#9cc21e;
  --lime-dark:#86a913;
  --ink:#222;
  --text:#555;
  --muted:#777;
  --line:#dcdcdc;
  --dark-band:#3b2f26;
  --caption:#4a4a4a;
  --white:#fff;
  --orange:#e89a1a;
}
*{box-sizing:border-box;margin:0;padding:0}
html,body{width:1200px;height:3543px;overflow:hidden}
body{position:relative;background:var(--white);font-family:"Roboto",sans-serif;color:var(--text)}
.abs{position:absolute}

/* header */
.site-header{position:absolute;left:0;top:0;width:1200px;height:245px;background:var(--white)}
.brand{position:absolute;left:0;width:1200px;top:52px;text-align:center}
.brand-name{display:inline-flex;align-items:center;gap:14px;font-family:"Raleway",sans-serif;font-weight:600;font-size:46px;color:var(--ink)}
.brand-mark{width:30px;height:30px;background:var(--lime);border-radius:50%}
.brand-tag{display:block;font-family:"Raleway",sans-serif;font-size:11px;letter-spacing:1px;color:var(--ink);margin-top:4px;font-weight:600}
.utility{position:absolute;left:850px;top:74px;display:flex;align-items:center;gap:28px;font-size:19px;color:#444}
.utility span{display:flex;align-items:center;gap:10px}
.main-nav{position:absolute;left:0;top:172px;width:1200px;display:flex;justify-content:center}
.main-nav a{font-family:"Roboto",sans-serif;font-size:15px;color:#555;text-decoration:none;letter-spacing:.3px;padding:0 32px;display:flex;align-items:center;gap:8px}
.caret{width:8px;height:8px}

/* hero */
.hero{position:absolute;left:0;top:245px;width:1200px;height:676px;background:linear-gradient(180deg,#5b92d6 0%,#b8d1ea 28%,#a99a82 45%,#c8bfae 60%,#6c8f3c 78%,#4f7a2a 100%)}
.hero-panel{position:absolute;left:106px;top:197px;width:490px;height:243px;background:rgba(30,30,30,.72);padding:40px 28px}
.hero-title{font-family:"Raleway",sans-serif;font-weight:500;font-size:42px;line-height:48px;color:var(--white);white-space:nowrap}
.hero-sub{font-family:"Raleway",sans-serif;font-size:15px;color:var(--white);margin-top:16px;letter-spacing:.5px;white-space:nowrap}
.hero-actions{display:flex;gap:20px;margin-top:28px}
.btn{display:inline-block;font-size:14px;padding:8px 14px;letter-spacing:.5px;color:var(--white);text-transform:uppercase}
.btn-fill{background:var(--lime)}
.btn-line{border:1px solid var(--white)}

/* section heads */
.section-title{position:absolute;left:0;width:1200px;text-align:center;font-family:"Raleway",sans-serif;font-weight:400;font-size:30px;color:#444;letter-spacing:1px}
.section-sub{position:absolute;left:0;width:1200px;text-align:center;font-size:13px;color:var(--muted)}

/* services */
.photo{position:absolute;box-shadow:0 4px 8px rgba(0,0,0,.25)}
.service-name{position:absolute;font-family:"Oswald",sans-serif;font-weight:500;font-size:20px;color:var(--ink);letter-spacing:.3px}
.service-text{position:absolute;width:300px;font-size:13px;line-height:19px;color:var(--muted)}
.read-more{position:absolute;font-size:15px;color:var(--lime);font-weight:500}

/* about */
.about{position:absolute;left:0;top:1531px;width:1200px;height:555px;background:linear-gradient(100deg,#2e2620,#4a3b2f 50%,#352a22)}
.about-copy{position:absolute;left:130px;top:140px;width:620px;font-size:14px;line-height:23px;color:var(--white)}
.about-copy ul{list-style:none;margin-top:18px}
.about-copy li{padding-left:30px;position:relative;line-height:30px}
.about-copy li::before{content:"";position:absolute;left:4px;top:13px;width:4px;height:4px;background:var(--white);border-radius:50%}

/* benefits */
.caption{position:absolute;height:107px;background:var(--caption);color:var(--white);font-size:13px;line-height:18px;text-align:center;padding:12px 16px}

/* faq */
.faq-list{position:absolute;left:149px;top:2730px;width:316px}
.faq-item{height:38px;border:1px solid var(--line);margin-bottom:14px;font-size:12px;color:#888;display:flex;align-items:center;padding-left:12px;gap:8px}
.faq-item.is-active{border-color:var(--orange);color:var(--orange)}
.dot{width:5px;height:5px;border-radius:50%;background:#bbb}
.is-active .dot{background:var(--orange)}
.faq-answer{position:absolute;left:489px;top:2728px;width:515px;height:303px;border:1px solid var(--line);padding:22px 18px}
.faq-answer h3{font-family:"Raleway",sans-serif;font-weight:600;font-size:17px;color:var(--orange);margin-bottom:12px}
.faq-answer p{font-size:13px;line-height:22px;color:var(--muted)}
.faq-answer .btn{margin-top:14px;font-size:13px}

/* map */
.map{position:absolute;left:0;top:3083px;width:1200px;height:389px;background:linear-gradient(135deg,#c9dcb0,#e6ead8 45%,#bcd4a0)}

/* footer */
.site-footer{position:absolute;left:0;top:3472px;width:1200px;height:71px;background:var(--lime);color:var(--white)}
.footer-links{position:absolute;left:130px;top:16px;display:flex;gap:18px;font-size:12px}
.copyright{position:absolute;left:130px;top:40px;font-size:11px}
.social{position:absolute;right:130px;top:24px;display:flex;gap:8px}
.social span{width:16px;height:16px;border-radius:50%;background:var(--white)}
</style>
</head>
<body>

<header class="site-header">
  <div class="brand">
    <span class="brand-name"><span class="brand-mark"></span>Korvanta</span>
    <span class="brand-tag">ADVANCED BUILDING TECHNOLOGY</span>
  </div>
  <div class="utility">
    <span><svg width="30" height="30" viewBox="0 0 30 30"><circle cx="15" cy="15" r="14" fill="var(--lime)"/><circle cx="15" cy="12" r="5" fill="#fff"/><path d="M6 24c2-5 16-5 18 0" fill="#fff"/></svg>Login <svg class="caret" viewBox="0 0 8 8"><path d="M1 2l3 3 3-3" stroke="#555" fill="none"/></svg></span>
    <span>English <svg class="caret" viewBox="0 0 8 8"><path d="M1 2l3 3 3-3" stroke="#555" fill="none"/></svg></span>
  </div>
  <nav class="main-nav">
    <a>HOME <svg class="caret" viewBox="0 0 8 8"><path d="M1 2l3 3 3-3" stroke="#555" fill="none"/></svg></a>
    <a>ABOUT US <svg class="caret" viewBox="0 0 8 8"><path d="M1 2l3 3 3-3" stroke="#555" fill="none"/></svg></a>
    <a>WHAT IS A SIP <svg class="caret" viewBox="0 0 8 8"><path d="M1 2l3 3 3-3" stroke="#555" fill="none"/></svg></a>
    <a>BENEFITS <svg class="caret" viewBox="0 0 8 8"><path d="M1 2l3 3 3-3" stroke="#555" fill="none"/></svg></a>
    <a>PHOTO GALLERY <svg class="caret" viewBox="0 0 8 8"><path d="M1 2l3 3 3-3" stroke="#555" fill="none"/></svg></a>
    <a>FAQ <svg class="caret" viewBox="0 0 8 8"><path d="M1 2l3 3 3-3" stroke="#555" fill="none"/></svg></a>
    <a>CONTACT US</a>
  </nav>
</header>

<section class="hero" role="img" aria-label="Large suburban family house with a green lawn and flower gardens under a blue sky">
  <div class="hero-panel">
    <h1 class="hero-title">YOUR DREAM HOUSE</h1>
    <p class="hero-sub">LOOKING FOR A QUALITY SIPS FOR YOUR HOUSE?</p>
    <div class="hero-actions"><span class="btn btn-fill">Our Services</span><span class="btn btn-line">Get a Quote</span></div>
  </div>
</section>

<h2 class="section-title" style="top:962px">OUR SERVICES</h2>
<p class="section-sub" style="top:1012px">We offer a unique design and project delivery service to develop your specific building requirements.</p>

<div class="photo" style="left:130px;top:1051px;width:298px;height:248px;background:linear-gradient(160deg,#d9cfc0,#f2c53a 40%,#3a3a3a)" role="img" aria-label="Two builders in hard hats"></div>
<div class="photo" style="left:451px;top:1051px;width:298px;height:248px;background:linear-gradient(160deg,#6fa8d8,#d7a870 50%,#a86f3c)" role="img" aria-label="Team raising a timber roof frame"></div>
<div class="photo" style="left:772px;top:1051px;width:303px;height:248px;background:linear-gradient(160deg,#e9e9e9,#b8b8b8 50%,#6b6b6b)" role="img" aria-label="Modern open-plan house interior"></div>

<h3 class="service-name" style="left:130px;top:1340px">BEST HOUSE RENOVATION</h3>
<h3 class="service-name" style="left:451px;top:1340px">TEAM WORK</h3>
<h3 class="service-name" style="left:772px;top:1340px">THE HOUSE BUILDING</h3>
<p class="service-text" style="left:130px;top:1388px">Lorem Ipsum is simply dummy text of the printing and typesetting industry. Lorem Ipsum has been the industry's standard dummy text ever since the 1500s</p>
<p class="service-text" style="left:451px;top:1388px">Lorem Ipsum is simply dummy text of the printing and typesetting industry. Lorem Ipsum has been the industry's standard dummy text ever since the 1500s</p>
<p class="service-text" style="left:772px;top:1388px">Lorem Ipsum is simply dummy text of the printing and typesetting industry. Lorem Ipsum has been the industry's standard dummy text ever since the 1500s</p>
<span class="read-more" style="left:130px;top:1472px">READ MORE</span>
<span class="read-more" style="left:451px;top:1470px">READ MORE</span>
<span class="read-more" style="left:772px;top:1470px">READ MORE</span>

<section class="about" role="img" aria-label="Blurred workshop background in dark brown tones">
  <h2 class="section-title" style="top:38px;color:var(--white)">ABOUT US</h2>
  <div class="about-copy">
    <p>korvanta are designers and manufacturers of an engineered structural insulated panel and concealed structural frame building product.<br>
    sips is rapidly becoming the building method of choice because of its overwhelming benefits and proven suitability.<br>
    korvanta panels can be used in residential and commercial building and are fully compliant to Australian standards.<br>
    We specialize in supplying on time and on budget, with high quality structural kits to builders and developers specific to their needs or requirements.</p>
    <ul>
      <li>High level of captive insulation. (warm in winter cool in summer)</li>
      <li>Very strong, light weight and durable.</li>
      <li>20 + year history of performance in cyclonic locations in WA</li>
      <li>Reduced build time (save time save money it's that easy)</li>
      <li>Energy efficient ( less energy to build and less energy to run ie lower power bills)</li>
    </ul>
  </div>
  <div class="photo" style="left:786px;top:146px;width:296px;height:293px;background:linear-gradient(160deg,#f0ede6,#f4c53b 45%,#c9b89a)" role="img" aria-label="Builder in a hard hat holding a power drill"></div>
</section>

<h2 class="section-title" style="top:2122px">OUR BENEFITS</h2>
<p class="section-sub" style="top:2172px">We offer a unique design and project delivery service to develop your specific building requirements.</p>

<div class="photo" style="left:134px;top:2211px;width:292px;height:246px;background:linear-gradient(160deg,#5b5b5b,#c7a060 55%,#e0c08a)" role="img" aria-label="Worker cutting timber with a circular saw"></div>
<div class="photo" style="left:455px;top:2211px;width:292px;height:246px;background:linear-gradient(160deg,#e8d2b0,#c79a62 55%,#8a6038)" role="img" aria-label="Hands measuring and marking timber with a pencil"></div>
<div class="photo" style="left:774px;top:2211px;width:292px;height:246px;background:linear-gradient(160deg,#d8cfc0,#c4a977 50%,#7a6a55)" role="img" aria-label="Worker on a ladder fitting insulated ceiling panels"></div>

<p class="caption" style="left:134px;top:2468px;width:292px">korvanta can also provide registered site assembly technicians to install walls or supervise/train your preferred subcontractor.</p>
<p class="caption" style="left:455px;top:2468px;width:292px">korvanta can arrange for the supply of a basic wall kit to full turn key build in accordance with all building license requirements.</p>
<p class="caption" style="left:774px;top:2468px;width:292px">korvanta supplies wall panel building kits to builders and owner builders for use in residential and commercial buildings are fully compliant to Australian standards.</p>

<h2 class="section-title" style="top:2632px">FAQ'S</h2>
<p class="section-sub" style="top:2682px">We offer a unique design and project delivery service to develop your specific building requirements.</p>

<div class="faq-list">
  <div class="faq-item"><span class="dot"></span>Do SIP homes require special foundations?</div>
  <div class="faq-item"><span class="dot"></span>How are windows and doors korvanta panels?</div>
  <div class="faq-item"><span class="dot"></span>How are plumbing and electrical wires fixed?</div>
  <div class="faq-item is-active"><span class="dot"></span>What kind of roofing can I use?</div>
  <div class="faq-item"><span class="dot"></span>Can I make additions to my home in the future?</div>
  <div class="faq-item"><span class="dot"></span>Are korvanta panel homes cheaper?</div>
</div>
<div class="faq-answer">
  <h3>NO. THEY CAN BE BUILT ON ALL TYPES OF FOUNDATIONS.</h3>
  <p>Lorem Ipsum is simply dummy text of the printing and typesetting industry. Lorem Ipsum has been the industry's standard dummy text ever since the 1500s, when an unknown printer took a galley of type and scrambled it to make a type specimen book. It has survived not only five centuries, but also the leap into electronic typesetting, remaining essentially unchanged. It was popularised in the 1960s with the release of Transfix sheets containing Lorem Ipsum passages, and more recently with desktop publishing software like Pagewise Composer including versions of Lorem Ipsum.</p>
  <span class="btn btn-fill">Learn More</span>
</div>

<section class="map" role="img" aria-label="Regional road map showing project locations">
  <svg class="abs" style="left:178px;top:38px" width="40" height="52" viewBox="0 0 40 52"><path d="M20 2C10 2 3 9 3 19c0 13 17 31 17 31s17-18 17-31C37 9 30 2 20 2z" fill="var(--lime)"/><circle cx="20" cy="19" r="7" fill="#fff"/></svg>
  <svg class="abs" style="left:275px;top:180px" width="40" height="52" viewBox="0 0 40 52"><path d="M20 2C10 2 3 9 3 19c0 13 17 31 17 31s17-18 17-31C37 9 30 2 20 2z" fill="var(--lime)"/><circle cx="20" cy="19" r="7" fill="#fff"/></svg>
  <svg class="abs" style="left:980px;top:90px" width="40" height="52" viewBox="0 0 40 52"><path d="M20 2C10 2 3 9 3 19c0 13 17 31 17 31s17-18 17-31C37 9 30 2 20 2z" fill="var(--lime)"/><circle cx="20" cy="19" r="7" fill="#fff"/></svg>
</section>

<footer class="site-footer">
  <nav class="footer-links"><span>Contact Us</span><span>Sitemap</span><span>Refer us your Friend</span><span>Feedback form</span><span>Your Home Design Guide</span><span>FAQ</span><span>Blog</span></nav>
  <p class="copyright">© 2016 Korvanta All rights reserved.</p>
  <div class="social"><span></span><span></span><span></span><span></span></div>
</footer>

</body>
</html>
```